Skyward Rovers

I would like to re-fresh my existing web page with something more elegant and professional and what will match with my new logo. From the page it should be clearly seen that I organize and sell flying safaris, it should not be tightened only to Africa, should be general.

Page to be re-freshed:
http://skyward-rovers.example

Target Market(s)

Pilots and non-pilots who are going to have a bush flying safari in Africa

Industry/Entity Type

It Professional

```html
<!DOCTYPE html>
<html lang="en">
<head>
<meta charset="utf-8">
<title>Skyward Rovers</title>
<link href="https://fonts.googleapis.com/css2?family=Federo&family=Open+Sans:wght@400;600&family=Questrial&display=swap" rel="stylesheet">
<style>
:root{
  --olive:#7a8c1e;
  --olive-light:#8ea126;
  --orange:#f26b0f;
  --ink:#222;
  --grey:#666;
  --pale:#f2f2f0;
  --footer:#26262b;
  --footer-bar:#1c1c20;
  --footer-text:#8a8a90;
  --white:#fff;
}
*{margin:0;padding:0;box-sizing:border-box}
html,body{width:932px;height:1200px;overflow:hidden;background:var(--white);font-family:"Open Sans",sans-serif;color:var(--ink)}
.page{position:relative;width:932px;height:1200px;overflow:hidden}
.abs{position:absolute}

/* header */
.header{left:0;top:0;width:932px;height:84px;background:#fafafa}
.brand{left:93px;top:24px;display:flex;align-items:center;gap:10px}
.brand-dot{width:34px;height:34px;border-radius:50%;background:var(--olive)}
.brand-name{font-family:"Federo",sans-serif;font-size:26px;color:var(--ink);line-height:1}
.ribbon{left:389px;top:32px;width:193px;height:21px;background:var(--ink);
  clip-path:polygon(0 0,100% 0,96% 50%,100% 100%,0 100%,4% 50%);
  display:flex;justify-content:center;align-items:center;font-size:8.5px;color:#fff;letter-spacing:.3px}
.ribbon span{padding:0 7px;border-left:1px solid #555}
.ribbon span:first-child{border-left:none}
.contact-top{left:676px;top:22px;font-size:17px;color:var(--ink)}
.contact-top .row{display:flex;align-items:center;gap:9px;margin-bottom:4px}
.contact-top .mail{font-size:12px}

/* nav */
.nav{left:0;top:84px;width:932px;height:34px;background:var(--olive);display:flex;align-items:center;padding-left:92px}
.nav a{color:#fff;text-decoration:none;font-size:13px;padding:0 9px;border-left:1px solid rgba(255,255,255,.25);line-height:18px}
.nav a:first-child{border-left:none;padding-left:9px}
.search{left:683px;top:91px;width:156px;height:21px;background:#fff}

/* hero */
.hero{left:0;top:118px;width:932px;height:369px;background:linear-gradient(180deg,#3a2a10 0%,#a56a14 35%,#d08a1e 55%,#5a3a0c 80%,#120c04 100%)}
.hero-panel{left:146px;top:303px;width:639px;height:132px;background:var(--orange);color:#fff;text-align:center;font-family:"Questrial",sans-serif}
.hero-panel .welcome{font-size:21px;margin-top:14px}
.hero-panel .title{font-family:"Federo",sans-serif;font-size:50px;line-height:1.05;margin-top:2px}
.hero-panel .tag{font-size:20px;margin-top:4px}
.slider-tab{left:692px;top:435px;width:93px;height:20px;background:var(--orange);display:flex;justify-content:center;align-items:center;gap:6px}
.slider-tab i{width:10px;height:10px;border-radius:50%;background:#fff;display:block;border:2px solid rgba(0,0,0,.15)}

/* about */
.about{left:0;top:487px;width:932px;height:281px;background:var(--pale)}
.about-photo{left:104px;top:550px;width:160px;height:160px;border-radius:50%;border:6px solid #fff;box-shadow:0 0 0 1px #ddd;background:linear-gradient(135deg,#9c8a6e,#5d6a3a)}
.about-title{left:335px;top:541px;font-family:"Federo",sans-serif;font-weight:400;font-size:31px;line-height:38px;color:var(--ink);white-space:nowrap}
.quote{font-family:Georgia,serif;font-size:60px;color:#d8d8d8;line-height:1}
.about-text{left:335px;width:482px;font-size:13.4px;line-height:15.5px;color:var(--grey);font-family:Arial,sans-serif}

/* tours */
.tours{left:0;top:768px;width:932px;height:234px;background:var(--olive);display:flex}
.tour{height:234px;text-align:center;color:#fff;position:relative;border-left:1px solid rgba(0,0,0,.08)}
.tour.active{background:var(--olive-light)}
.tour h3{font-family:"Federo",sans-serif;font-weight:400;font-size:15px;margin-top:16px}
.tour .pic{width:133px;height:133px;border-radius:50%;border:4px solid #fff;margin:13px auto 0}
.tour p{font-size:9.3px;line-height:12px;margin:11px auto 0;width:150px;font-family:Arial,sans-serif}

/* footer */
.footer{left:0;top:1002px;width:932px;height:172px;background:var(--footer)}
.fcol{top:1032px;color:var(--footer-text)}
.fcol h4{font-family:"Federo",sans-serif;font-weight:400;font-size:17px;color:#fff;margin-bottom:10px;white-space:nowrap}
.sitemap li{list-style:none;font-size:9.5px;line-height:13.5px}
.fcontact{font-size:12px;line-height:16px}
.fcontact .phone{font-size:17px;color:#fff;display:flex;align-items:center;gap:8px;margin:6px 0 4px}
.fcontact .mail{display:flex;align-items:center;gap:8px}
.news p{font-size:9.5px;line-height:13px;width:180px}
.news .field{width:175px;height:22px;background:#ddd;margin-top:10px;font-size:9.5px;font-style:italic;color:#777;padding:5px 0 0 28px}
.news .btn{display:inline-block;background:var(--orange);color:#fff;font-size:13px;padding:3px 12px;margin-top:8px}
.social .row{display:flex;align-items:center;gap:10px;font-size:9.5px;margin-bottom:6px}
.social .dot{width:21px;height:21px;border-radius:50%;background:#3d6da8;border:2px solid #555}
.bottom{left:0;top:1174px;width:932px;height:26px;background:var(--footer-bar);border-top:1px solid #333;font-size:9.5px;color:#888;padding:7px 0 0 93px}
</style>
</head>
<body>
<div class="page">

  <header class="abs header"></header>
  <div class="abs brand"><span class="brand-dot"></span><span class="brand-name">Skyward Rovers</span></div>
  <div class="abs ribbon"><span>TRAINING</span><span>PPL VALIDATION</span><span>GALLERY</span></div>
  <div class="abs contact-top">
    <div class="row">
      <svg width="10" height="15" viewBox="0 0 10 15"><rect x="1" y="1" width="8" height="13" rx="1.5" fill="none" stroke="#222" stroke-width="1.6"/><rect x="4" y="11" width="2" height="1.5" fill="#222"/></svg>
      +41 70 555 01 23
    </div>
    <div class="row mail">
      <svg width="12" height="9" viewBox="0 0 12 9"><rect width="12" height="9" fill="#333"/><path d="M0 0l6 5 6-5" fill="none" stroke="#fff"/></svg>
      info@skyward-rovers.example
    </div>
  </div>

  <nav class="abs nav">
    <a>Home</a><a>Guided Tours</a><a>Self Guided Tours</a><a>Sample Tours</a><a>Build Your Trip</a><a>Contact</a>
  </nav>
  <div class="abs search">
    <svg class="abs" style="right:6px;top:5px" width="10" height="10" viewBox="0 0 10 10"><circle cx="4" cy="4" r="3" fill="none" stroke="#bbb" stroke-width="1.5"/><path d="M6.5 6.5L9.5 9.5" stroke="#bbb" stroke-width="1.5"/></svg>
  </div>

  <section class="abs hero" role="img" aria-label="Savanna at sunset with a giraffe and acacia trees in silhouette"></section>
  <div class="abs hero-panel">
    <div class="welcome">Welcome to the world of</div>
    <div class="title">Skyward Rovers</div>
    <div class="tag">for the adventure of a lifetime</div>
  </div>
  <div class="abs slider-tab"><i></i><i></i><i></i></div>

  <section class="abs about"></section>
  <div class="abs about-photo" role="img" aria-label="Group of travellers sitting together on rocks during a safari"></div>
  <div class="abs quote" style="left:305px;top:532px">&ldquo;</div>
  <h2 class="abs about-title">About Skyward Rovers</h2>
  <p class="abs about-text" style="top:589px">organises and facilitates self-fly safaris through Southern Africa. What better way to see the wonders of this land than from the pilot's seat of your own aircraft. Whether you're a PPL wanting to experience something beyond flying circuits at your local airfield, a seasoned ATP looking to recapture that passion for flying, or a traveller wanting to<br>experience</p>
  <p class="abs about-text" style="top:694px">Africa from a bird's perspective, alone or as part of a group, the flying in this part of the world offers a truly rewarding and unforgettable experience.</p>
  <div class="abs quote" style="left:810px;top:692px">&rdquo;</div>

  <section class="abs tours">
    <div class="tour" style="width:280px;border-left:none">
      <h3>Guided Tours</h3>
      <div class="pic" role="img" aria-label="Travellers silhouetted against a sunset" style="background:linear-gradient(180deg,#e0902a,#5a2a0a)"></div>
      <p>For the social pilot who wants to enjoy a luxury safari flying in the bush</p>
    </div>
    <div class="tour active" style="width:186px">
      <h3>Self Guided Tours</h3>
      <div class="pic" role="img" aria-label="Light aircraft parked on a bush airstrip" style="background:linear-gradient(180deg,#8aa0b8,#c8c4b8)"></div>
      <p>For the more adventurous and experienced pilot, wanting to set off on his/her own</p>
    </div>
    <div class="tour" style="width:186px">
      <h3>Sample Tours</h3>
      <div class="pic" role="img" aria-label="Lion resting in the grass" style="background:linear-gradient(135deg,#c89040,#6a4a1a)"></div>
      <p>Check our sample tours to give your the feeling of the options</p>
    </div>
    <div class="tour" style="width:280px">
      <h3>Build Your Trip</h3>
      <div class="pic" role="img" aria-label="Pilots standing beside their aircraft" style="background:linear-gradient(180deg,#b8cce0,#9a9a80)"></div>
      <p>Try to design your own tour so we can review and send an offer accordingly</p>
    </div>
  </section>

  <footer class="abs footer"></footer>
  <div class="abs fcol sitemap" style="left:93px">
    <h4>Site Map</h4>
    <ul><li>Home</li><li>Guided Tours</li><li>Self Guided Tours</li><li>Sample Tours</li><li>Build Your Trip</li><li>Contact</li></ul>
  </div>
  <div class="abs fcol fcontact" style="left:222px">
    <h4>Skyward Rovers Contact</h4>
    <div>Tomas Varga<br>Alpendorf, Switzerland</div>
    <div class="phone">
      <svg width="9" height="14" viewBox="0 0 10 15"><rect x="1" y="1" width="8" height="13" rx="1.5" fill="none" stroke="#fff" stroke-width="1.6"/></svg>
      +41 70 555 01 23
    </div>
    <div class="mail">
      <svg width="11" height="8" viewBox="0 0 12 9"><rect width="12" height="9" fill="#888"/><path d="M0 0l6 5 6-5" fill="none" stroke="#26262b"/></svg>
      info@skyward-rovers.example
    </div>
  </div>
  <div class="abs fcol news" style="left:480px">
    <h4>Newsletter</h4>
    <p>Lorem Ipsum is simply dummy text of the printing and typesetting industry.</p>
    <div class="field">Email Address</div>
    <span class="btn">Subscribe Now</span>
  </div>
  <div class="abs fcol social" style="left:705px">
    <h4>Follow Us On</h4>
    <div class="row"><span class="dot"></span>Follow us on Friendbook</div>
    <div class="row"><span class="dot" style="background:#2a9ad8"></span>Follow us on Chirper</div>
    <div class="row"><span class="dot" style="background:#1f6fa8"></span>Join us on WorkLink</div>
  </div>
  <div class="abs bottom">Copyright &copy; 2012-2013 skyward-rovers.example</div>

</div>
</body>
</html>
```